Brindle Logistics Business Card Design

We are a trucking and warehousing company. We run freight in the US manly from the Pacific NW to TX and back up the the PNW. We also do warehousing where we store, move, and distribute freight. Looking for a clean and modern design of business card. We would like to look rich and elegant. Attached is our logo.

Industry/Entity Type

Trucking Company

Contact Information for Business Card

Looking for a clean and modern design of business card. We would like to look rich and elegant.

Font styles to use
Sans Serif

Colors

Designer to choose colors to be used in the design.

Requirements
Must have
• logo but it should not dominate the card
Should not have
• logo should not dominate the card

```html
<!DOCTYPE html>
<html lang="en">
<head>
<meta charset="utf-8">
<title>Brindle Logistics Business Card</title>
<link rel="stylesheet" href="https://fonts.googleapis.com/css2?family=Nunito+Sans:wght@300;400;700;800&display=swap">
<style>
  :root {
    --backdrop: #2a5f8c;
    --card-white: #eef0f1;
    --brand-blue: #0a74b4;
    --brand-cyan: #1fb6ee;
    --brand-sky: #4fcaf5;
    --ink: #333a40;
    --accent-gold: #e0a019;
    --line-light: #d7f0fb;
  }
  * { box-sizing: border-box; margin: 0; padding: 0; }
  html, body { width: 1200px; height: 1200px; overflow: hidden; }
  body {
    background: var(--backdrop);
    font-family: "Nunito Sans", Arial, sans-serif;
    display: flex;
    flex-direction: column;
    align-items: center;
    justify-content: center;
    gap: 60px;
  }
  .card {
    width: 840px;
    height: 480px;
    position: relative;
    overflow: hidden;
    box-shadow: 0 10px 30px rgba(0,0,0,0.25);
  }
  /* Front */
  .card-front { background: var(--card-white); color: var(--ink); }
  .brand {
    position: absolute; left: 70px; top: 90px;
    display: flex; align-items: center; gap: 16px;
  }
  .brand-dot { width: 46px; height: 46px; border-radius: 50%; background: var(--brand-blue); }
  .brand-name {
    font-weight: 800; font-size: 34px; letter-spacing: 1px;
    color: var(--brand-blue); line-height: 1.05; text-transform: uppercase;
  }
  .person { position: absolute; left: 470px; top: 175px; font-size: 22px; line-height: 1.4; }
  .person-name { font-weight: 800; font-size: 30px; color: var(--brand-blue); }
  .label { color: var(--accent-gold); font-weight: 800; margin-right: 6px; }
  .office { position: absolute; left: 70px; bottom: 60px; font-size: 22px; line-height: 1.45; }
  .office-phones { padding-left: 40px; display: flex; gap: 36px; }
  .hotline {
    position: absolute; left: 580px; bottom: 60px;
    border-left: 3px solid var(--brand-blue); padding-left: 14px;
    font-size: 22px; line-height: 1.45;
  }
  .hotline-number { font-weight: 800; color: var(--ink); }
  .hotline-web { font-weight: 700; color: var(--brand-blue); }
  /* Back */
  .card-back {
    background: linear-gradient(135deg, #0b7cc0 0%, var(--brand-blue) 60%, #08679f 100%);
  }
  .mascot-art {
    position: absolute; inset: 0;
    width: 840px; height: 480px;
  }
  .route {
    position: absolute; left: 290px; bottom: 44px;
    color: var(--line-light); font-size: 24px; font-weight: 300; letter-spacing: 4px;
    display: flex; align-items: center; gap: 12px;
  }
</style>
</head>
<body>
  <section class="card card-front">
    <div class="brand">
      <span class="brand-dot"></span>
      <span class="brand-name">Brindle<br>Logistics, LLC</span>
    </div>
    <div class="person">
      <div class="person-name">Daniel Reyes</div>
      <div>Chief Financial Officer</div>
      <div><span class="label">e</span>dreyes@brindlelogistics.com</div>
      <div><span class="label">c</span>360-555-0147</div>
    </div>
    <div class="office">
      <div>4820 NE Alder Ct, Ridgefield, WA 98642</div>
      <div class="office-phones">
        <span><span class="label">p</span>360-555-0120</span>
        <span><span class="label">f</span>360-555-0133</span>
      </div>
    </div>
    <div class="hotline">
      <div class="hotline-number">1-855-555-0199</div>
      <div class="hotline-web">brindlelogistics.com</div>
    </div>
  </section>

  <section class="card card-back">
    <svg class="mascot-art" viewBox="0 0 840 480" role="img" aria-label="Large stylised bird-of-prey head illustration in light cyan tones, filling the left of the card">
      <defs>
        <radialGradient id="mascotGlow" cx="0.3" cy="0.4" r="0.62" gradientUnits="objectBoundingBox">
          <stop offset="0" stop-color="#4fcaf5" stop-opacity="0.95"/>
          <stop offset="0.45" stop-color="#1fb6ee" stop-opacity="0.7"/>
          <stop offset="1" stop-color="#0a74b4" stop-opacity="0"/>
        </radialGradient>
      </defs>
      <rect width="840" height="480" fill="url(#mascotGlow)"/>
    </svg>
    <div class="route">
      <span>PACIFIC NORTHWEST</span>
      <svg width="28" height="16" viewBox="0 0 28 16" aria-hidden="true">
        <path d="M0 8 L9 1 V15 Z M28 8 L19 1 V15 Z" fill="#e0a019"/>
        <rect x="8" y="6" width="12" height="4" fill="#e0a019"/>
      </svg>
      <span>TEXAS</span>
    </div>
  </section>
</body>
</html>
```